Construction proffessionals servicing the inner suburbs of Melbournes NorthWest specialising in aler

I would like a web site that is sharp, contemporary and simple to navigate, ie.not too many pages. i would like a home page with some info about us, who we are what our history is and my passion for building and construction based on impeccable customer focus. i would like a projects page and somewhere for clients to add testimonials. i would like a project calculator as well so prospective clients can work out a rough budget prior to contacting. i would like the colours to be in line with my logo which i have uploaded. i have many photos which can be used and can be shared via drop box when required. I would like it to be personal to capture our transparent process. i would like to add our company process as well. be brave and take risks.

Target Market(s)

People renovating and extending their homes, people needing inspections on new homes and pre-purchase inspections

Industry/Entity Type

Construction

Number of Pages Required

5+ page

Requirements
Must have
• Professional, easy to navigate, provide viewers with a happy experience, look great, contacts, project calculator, link through to my training company www.ktrp.vic.edu.au also check ormwaybuilds on instagram for pics
Nice to have
• Links to instagram, fonts to match email signature

```html
<!DOCTYPE html>
<html lang="en">
<head>
<meta charset="utf-8">
<title>Ormway Builds – Home Renovation</title>
<link href="https://fonts.googleapis.com/css2?family=Open+Sans:ital,wght@0,400;0,600;0,700;0,800;1,400;1,600;1,700;1,800&display=swap" rel="stylesheet">
<style>
:root{
  --orange:#f7941d;
  --orange-deep:#e8850f;
  --charcoal:#5b5753;
  --footer:#6b6661;
  --ink:#333;
  --muted:#777;
  --white:#fff;
}
*{box-sizing:border-box;margin:0;padding:0}
html,body{width:698px;height:1200px;overflow:hidden;background:var(--white)}
body{font-family:"Open Sans",Arial,sans-serif;color:var(--ink);position:relative}

.site-header{position:absolute;top:0;left:0;width:698px;height:93px;background:var(--white)}
.brand{position:absolute;left:75px;top:22px;display:flex;align-items:center;gap:8px;font-weight:800;font-size:26px;color:var(--orange)}
.brand-mark{width:22px;height:22px;background:var(--orange)}
.main-nav{position:absolute;right:42px;top:38px;display:flex;gap:14px;align-items:center;font-size:10px;font-weight:600;text-transform:uppercase;color:var(--ink)}

.hero{position:absolute;top:93px;left:0;width:698px;height:395px;
  background:linear-gradient(160deg,#8a8580 0%,#5e564e 40%,#3d342c 70%,#6b4a2e 100%)}
.hero-title{position:absolute;top:92px;width:100%;text-align:center;font-size:45px;font-weight:800;font-style:italic;color:var(--white);letter-spacing:.5px}
.hero-text{position:absolute;top:168px;left:220px;width:260px;text-align:center;font-size:15px;font-style:italic;line-height:21px;color:var(--white)}
.btn-go{position:absolute;top:297px;left:280px;width:140px;height:56px;border-radius:28px;background:var(--orange);border:4px solid var(--charcoal);color:var(--white);font-size:30px;font-weight:800;display:flex;align-items:center;justify-content:center}

.services{position:absolute;top:488px;left:0;width:698px;height:330px}
.service{position:absolute;top:35px;width:170px;text-align:center}
.service-icon{width:100px;height:117px;margin:0 auto;background:linear-gradient(#6a6560,#f7941d);border-radius:4px}
.service h3{margin-top:16px;font-size:8px;font-weight:800;text-transform:uppercase}
.service .tagline{font-size:6px;color:var(--muted);margin-top:3px}
.service .author{font-size:11px;font-style:italic;color:var(--muted);margin-top:5px}
.service p{font-size:6px;line-height:9px;color:var(--muted);margin:6px auto 0;width:140px}
.btn-read{display:inline-block;margin-top:22px;width:102px;height:18px;line-height:14px;background:var(--charcoal);border:2px solid var(--orange);color:var(--white);font-size:10px;font-weight:800;text-transform:uppercase}

.promo{position:absolute;top:842px;left:0;width:698px;height:193px;background:var(--orange);text-align:center;color:var(--white)}
.promo h2{margin-top:18px;font-size:25px;font-weight:800;font-style:italic}
.promo p{margin:8px auto 0;width:470px;font-size:15px;font-style:italic;font-weight:600;line-height:21px}
.btn-learn{display:inline-block;margin-top:14px;width:150px;height:29px;line-height:29px;background:var(--charcoal);font-size:14px;font-weight:800;letter-spacing:1px}

.site-footer{position:absolute;top:1035px;left:0;width:698px;height:165px;background:var(--footer)}
.footer-col{position:absolute;top:38px;font-size:9px;line-height:14px;color:var(--white)}
.footer-col h4{font-size:7px;font-weight:700;color:var(--orange);text-transform:uppercase;margin-bottom:4px}
.footer-col .accent{color:var(--orange)}
.copyright{position:absolute;bottom:8px;width:100%;text-align:center;font-size:7px;color:var(--orange)}
</style>
</head>
<body>
<header class="site-header">
  <div class="brand"><span class="brand-mark"></span>Ormway</div>
  <nav class="main-nav">
    <span>Home</span><span>Services</span><span>Project Gallery</span><span>Consulting</span><span>Contact</span>
    <svg width="12" height="12" viewBox="0 0 12 12" aria-label="Search"><circle cx="5" cy="5" r="3.6" fill="none" stroke="#333" stroke-width="1.6"/><line x1="7.7" y1="7.7" x2="11" y2="11" stroke="#333" stroke-width="1.8"/></svg>
  </nav>
</header>

<section class="hero" role="img" aria-label="Photo of a renovated modern living room with sofa and timber floor">
  <h1 class="hero-title">HOME RENOVATION</h1>
  <p class="hero-text">Lorem ipsum dolor sit amet, cibo senserit rationibus eu usu. Regione aperiri sea te, per ei everti fierent. Atqui omnes minimum his id.</p>
  <div class="btn-go">GO!</div>
</section>

<section class="services">
  <div class="service" style="left:66px">
    <div class="service-icon" role="img" aria-label="Illustration of a builder carrying a beam"></div>
    <h3>Lorem ipsum dolor</h3>
    <div class="tagline">Et graeco sint ius mea nostro dolorem</div>
    <div class="author">Name Surname</div>
    <p>Sed fugit libris eu quo probo utamur nostrud inermis vix, mei ad tantas ponderum.</p>
    <span class="btn-read">Read more</span>
  </div>
  <div class="service" style="left:264px">
    <div class="service-icon" role="img" aria-label="Illustration of a house"></div>
    <h3>Lorem ipsum dolor</h3>
    <div class="tagline">Et graeco sint ius mea nostro dolorem</div>
    <div class="author">Name Surname</div>
    <p>Sed fugit libris eu quo probo utamur nostrud inermis vix, mei ad tantas ponderum.</p>
    <span class="btn-read">Read more</span>
  </div>
  <div class="service" style="left:462px">
    <div class="service-icon" role="img" aria-label="Illustration of a paint roller"></div>
    <h3>Lorem ipsum dolor</h3>
    <div class="tagline">Et graeco sint ius mea nostro dolorem</div>
    <div class="author">Name Surname</div>
    <p>Sed fugit libris eu quo probo utamur nostrud inermis vix, mei ad tantas ponderum.</p>
    <span class="btn-read">Read more</span>
  </div>
</section>

<section class="promo">
  <h2>Ei nostrud adipisci scripserit</h2>
  <p>Nulla eirmod iustico est in, odio placerat pri eu, id eum esse sensibus. Ex vis case summo menandri.</p>
  <span class="btn-learn">LEARN MORE</span>
</section>

<footer class="site-footer">
  <div class="footer-col" style="left:151px"><h4>Our Stuff</h4>Gift Certificates<br>Referrals<br>Training Center</div>
  <div class="footer-col" style="left:263px"><h4>Support</h4>FAQ<br>Feedback<br>Contact<br>How it Works<br><span class="accent">Testimonials</span></div>
  <div class="footer-col" style="left:365px"><h4>Company</h4>About Us<br>Partnership<br>Blog</div>
  <div class="footer-col" style="left:465px"><h4>Our Stuff</h4>Gift Certificates<br>Referrals<br>Training Center</div>
  <div class="copyright">Copyright ©</div>
</footer>
</body>
</html>
```